Executive Business Card for Healthcare Company [Need Today]

I need a business card design for a healthcare company. The only branding the company has thus far is a logo. The cards will be utilized by company executives. The design I envision will be vibrant and appealing but with a corporate feel. They shouldn't be too casual or playful. I would like to complete this project TODAY if possible.

Target Market(s)

Healthcare vendors, other executives in healthcare and pharmaceuticals

Industry/Entity Type

Pharmaceutical

Contact Information for Business Card

See attachment

Font styles to use
Serif
Sans Serif

Colors

Designer to choose colors to be used in the design.

```html
<!DOCTYPE html>
<html lang="en">
<head>
<meta charset="utf-8">
<title>Quillmoor Therapeutics – Business Card</title>
<link rel="stylesheet" href="https://fonts.googleapis.com/css2?family=Red+Hat+Display:wght@400;500;700&display=swap">
<style>
  :root {
    --backdrop: #c3c3be;
    --card: #eaebea;
    --teal: #3cc1c7;
    --teal-ring: #5ec49a;
    --ink: #6b6b6b;
    --ink-soft: #8a8a8a;
    --rule: #b9b9b9;
  }
  * { margin: 0; padding: 0; box-sizing: border-box; }
  html, body { width: 1200px; height: 1000px; overflow: hidden; }
  body {
    position: relative;
    background: var(--backdrop);
    font-family: "Red Hat Display", "Helvetica Neue", Arial, sans-serif;
    color: var(--ink);
  }
  .card {
    position: absolute;
    width: 523px;
    height: 297px;
    background: var(--card);
    overflow: hidden;
  }
  .card--front { left: 299px; top: 157px; }
  .card--back { left: 478px; top: 536px; }

  /* Front */
  .brand {
    position: absolute;
    left: 122px;
    top: 104px;
    display: flex;
    align-items: center;
    gap: 18px;
  }
  .brand__mark {
    width: 88px;
    height: 88px;
    border-radius: 50%;
    border: 3px solid var(--teal-ring);
    flex: none;
  }
  .brand__name {
    font-size: 28px;
    font-weight: 500;
    line-height: 1.05;
    color: var(--teal);
    letter-spacing: 0.3px;
  }

  /* Back */
  .holder {
    position: absolute;
    left: 34px;
    top: 105px;
  }
  .holder__name {
    font-size: 15px;
    font-weight: 700;
    letter-spacing: 0.6px;
    text-transform: uppercase;
    color: var(--ink);
  }
  .holder__title {
    margin-top: 3px;
    font-size: 15px;
    font-weight: 400;
    color: var(--ink-soft);
  }
  .divider {
    position: absolute;
    left: 261px;
    top: 50px;
    width: 1px;
    height: 152px;
    background: var(--rule);
  }
  .contact {
    position: absolute;
    left: 280px;
    list-style: none;
    font-size: 15px;
    line-height: 20px;
    color: var(--ink-soft);
  }
  .contact li { position: relative; padding-left: 31px; }
  .contact svg {
    position: absolute;
    left: 0;
    top: 3px;
    width: 14px;
    height: 14px;
    fill: var(--ink-soft);
  }
  .contact strong { font-weight: 700; color: var(--ink); }
  .contact--phone { top: 45px; }
  .contact--email { top: 104px; }
  .contact--address { top: 146px; }
  .accent-band {
    position: absolute;
    left: 0;
    bottom: 0;
    width: 523px;
    height: 66px;
    background: linear-gradient(to bottom, rgba(60, 193, 199, 0) 0%, rgba(60, 193, 199, 0.55) 45%, var(--teal) 100%);
  }
</style>
</head>
<body>

<section class="card card--front" aria-label="Card front">
  <div class="brand">
    <span class="brand__mark"></span>
    <span class="brand__name">Quillmoor<br>Therapeutics</span>
  </div>
</section>

<section class="card card--back" aria-label="Card back">
  <div class="holder">
    <p class="holder__name">Daniel Marsh</p>
    <p class="holder__title">Senior Director of Marketing</p>
  </div>

  <span class="divider"></span>

  <ul class="contact contact--phone">
    <li>
      <svg viewBox="0 0 24 24" aria-hidden="true"><path d="M6.6 10.8a15.1 15.1 0 0 0 6.6 6.6l2.2-2.2a1 1 0 0 1 1-.25 11.4 11.4 0 0 0 3.6.57 1 1 0 0 1 1 1V20a1 1 0 0 1-1 1A17 17 0 0 1 3 4a1 1 0 0 1 1-1h3.5a1 1 0 0 1 1 1c0 1.25.2 2.450.57 3.57a1 1 0 0 1-.25 1z"/></svg>
      <strong>555-201-4870</strong> office<br><strong>555-382-1645</strong> cell
    </li>
  </ul>

  <ul class="contact contact--email">
    <li>
      <svg viewBox="0 0 24 24" aria-hidden="true"><path d="M2 5h20v14H2z M3.5 6.5 12 12.5l8.5-6z" fill-rule="evenodd"/></svg>
      dmarsh@quillmoorrx.com
    </li>
  </ul>

  <ul class="contact contact--address">
    <li>
      <svg viewBox="0 0 24 24" aria-hidden="true"><path d="M12 2a7 7 0 0 0-7 7c0 5 7 13 7 13s7-8 7-13a7 7 0 0 0-7-7zm0 9.5A2.5 2.5 0 1 1 12 6.5a2.5 2.5 0 0 1 0 5z"/></svg>
      <strong>Quillmoor Therapeutics, LLC</strong><br>118 W Harmon Avenue<br>Greenfield, GA 30012
    </li>
  </ul>

  <div class="accent-band" role="img" aria-label="Decorative teal wave band along the card bottom"></div>
</section>

</body>
</html>
```